Business Cards Design for the electrical wholesaler: clean bold dynamic :)

We need a business card design that would follow our latest brand guidelines. As an electrical wholesaler we want to bring a fresh look and feel into the industry. The design should be clean bold and dynamic. It should come alive with the renewed energy of our green colour. Our grey colour should keep things balanced and complement the notion of maturity and responsibility. We employ Lato as a corporate font however are not bound by this font and we’re open to interpretation here.

Target Market(s)

Electrical contractors

Industry/Entity Type

Business

Contact Information for Business Card

Logo
Name & Surname: Olena Dovbush
Job Title: Director of Marketing
Email: helen.dovbush@mailvane.example
Cell phone: XXX.XXX.XXXX
Address: 20917 - 87 Ave. Edmonton, AB, Canada. T6K 2R8
Business Phone: 780.555.0187
Website: www.qorvil.example

Font styles to use
Other font styles liked:
• Lato

Requirements
Must have
• Logo & website
Nice to have
• Brand elements - some of them you may find in the attached Brand Guidelines (e.g. three lines on the background signifying "W")

```html
<!DOCTYPE html>
<html lang="en">
<head>
<meta charset="utf-8">
<title>Qorvil Business Cards</title>
<link rel="stylesheet" href="https://fonts.googleapis.com/css2?family=Lato:wght@400;700&family=Open+Sans:wght@400&display=swap">
<style>
  :root {
    --green: #8cc63f;
    --green-deep: #6aa62c;
    --green-pale: #e8f3da;
    --grey: #4d4d4f;
    --grey-soft: #5c5c5e;
    --bg: #ececec;
    --white: #ffffff;
  }
  * { margin: 0; padding: 0; box-sizing: border-box; }
  html, body { width: 1200px; height: 900px; overflow: hidden; }
  body {
    background: var(--bg);
    position: relative;
    font-family: "Lato", sans-serif;
    color: var(--grey);
  }
  .side-label {
    position: absolute;
    top: 182px;
    font-family: "Open Sans", sans-serif;
    font-size: 30px;
    color: var(--grey-soft);
  }
  .side-label--back { left: 262px; }
  .side-label--front { left: 842px; }

  .card {
    position: absolute;
    top: 250px;
    width: 320px;
    height: 540px;
    box-shadow: 0 10px 24px rgba(0,0,0,0.14);
  }
  .card--back {
    left: 220px;
    background: linear-gradient(160deg, var(--green-deep) 0%, var(--green) 45%, var(--green) 100%);
    display: flex;
    align-items: center;
    justify-content: center;
  }
  .brand {
    display: flex;
    align-items: center;
    gap: 10px;
    font-family: "Lato", sans-serif;
    font-weight: 700;
    letter-spacing: -0.5px;
  }
  .brand__square {
    display: block;
    background: currentColor;
    border-radius: 3px;
  }
  .card--back .brand { color: var(--white); font-size: 52px; }
  .card--back .brand__square { width: 38px; height: 38px; }

  .card--front {
    left: 660px;
    background: var(--white);
  }
  .card--front .brand {
    position: absolute;
    top: 40px;
    left: 0; right: 0;
    justify-content: center;
    color: var(--grey);
    font-size: 40px;
  }
  .card--front .brand__square { width: 28px; height: 28px; background: var(--green); }

  .front__band {
    position: absolute;
    top: 128px;
    left: 0;
    width: 100%;
    height: 68px;
    background: var(--green);
  }
  .front__avatar {
    position: absolute;
    top: 112px;
    left: 50%;
    width: 100px;
    height: 100px;
    margin-left: -50px;
    border-radius: 50%;
    border: 5px solid var(--white);
    background: var(--green);
  }
  .front__person {
    position: absolute;
    top: 232px;
    left: 0; right: 0;
    text-align: center;
    font-variant: small-caps;
  }
  .person__name {
    font-size: 32px;
    font-weight: 700;
    color: var(--green);
    letter-spacing: 1px;
  }
  .person__title {
    font-size: 16px;
    color: var(--grey);
    letter-spacing: 0.5px;
  }

  .contact-list {
    position: absolute;
    top: 322px;
    left: 28px;
    right: 16px;
    list-style: none;
  }
  .contact-list li {
    display: flex;
    align-items: center;
    gap: 12px;
    height: 42px;
    margin-bottom: 3px;
    font-size: 13.5px;
    color: var(--grey);
    line-height: 1.25;
  }
  .contact-icon {
    flex: 0 0 36px;
    width: 36px;
    height: 36px;
  }
</style>
</head>
<body>
  <div class="side-label side-label--back">Back Side</div>
  <div class="side-label side-label--front">Front Side</div>

  <section class="card card--back" aria-label="Card back">
    <div class="brand"><span class="brand__square"></span>qorvil</div>
  </section>

  <section class="card card--front" aria-label="Card front">
    <div class="brand"><span class="brand__square"></span>qorvil</div>
    <div class="front__band"></div>
    <div class="front__avatar" role="img" aria-label="Profile photo placeholder"></div>

    <div class="front__person">
      <div class="person__name">Olena Dovbush</div>
      <div class="person__title">Director of Marketing</div>
    </div>

    <ul class="contact-list">
      <li>
        <svg class="contact-icon" viewBox="0 0 36 36" aria-hidden="true">
          <circle cx="18" cy="18" r="18" fill="#8cc63f"/>
          <rect x="9" y="12" width="18" height="12" fill="none" stroke="#4d4d4f" stroke-width="2"/>
          <path d="M9 12 L18 19 L27 12" fill="none" stroke="#4d4d4f" stroke-width="2"/>
        </svg>
        helen.dovbush@mailvane.example
      </li>
      <li>
        <svg class="contact-icon" viewBox="0 0 36 36" aria-hidden="true">
          <circle cx="18" cy="18" r="18" fill="#8cc63f"/>
          <path d="M12 10 l4 0 l2 5 l-3 2 a10 10 0 0 0 5 5 l2 -3 l5 2 l0 4 a2 2 0 0 1 -2 2 a16 16 0 0 1 -15 -15 a2 2 0 0 1 2 -2 z" fill="#4d4d4f"/>
        </svg>
        XXX.XXX.XXXX
      </li>
      <li>
        <svg class="contact-icon" viewBox="0 0 36 36" aria-hidden="true">
          <circle cx="18" cy="18" r="18" fill="#8cc63f"/>
          <path d="M18 8 a6 6 0 0 1 6 6 c0 5 -6 11 -6 11 c0 0 -6 -6 -6 -11 a6 6 0 0 1 6 -6 z" fill="#4d4d4f"/>
          <circle cx="18" cy="14" r="2.2" fill="#8cc63f"/>
          <path d="M9 28 h18" stroke="#4d4d4f" stroke-width="2"/>
        </svg>
        <span>20917 - 87 Ave. Edmonton, AB,<br>Canada. T6K 2R8</span>
      </li>
      <li>
        <svg class="contact-icon" viewBox="0 0 36 36" aria-hidden="true">
          <circle cx="18" cy="18" r="18" fill="#8cc63f"/>
          <rect x="9" y="13" width="5" height="14" rx="1" fill="#4d4d4f"/>
          <rect x="15" y="11" width="12" height="16" rx="1" fill="#4d4d4f"/>
          <rect x="17" y="13" width="8" height="4" fill="#8cc63f"/>
          <g fill="#8cc63f"><rect x="17" y="19" width="2" height="2"/><rect x="20" y="19" width="2" height="2"/><rect x="23" y="19" width="2" height="2"/><rect x="17" y="23" width="2" height="2"/><rect x="20" y="23" width="2" height="2"/><rect x="23" y="23" width="2" height="2"/></g>
        </svg>
        780.555.0187
      </li>
      <li>
        <svg class="contact-icon" viewBox="0 0 36 36" aria-hidden="true">
          <circle cx="18" cy="18" r="18" fill="#8cc63f"/>
          <circle cx="18" cy="18" r="9" fill="none" stroke="#4d4d4f" stroke-width="2"/>
          <ellipse cx="18" cy="18" rx="4" ry="9" fill="none" stroke="#4d4d4f" stroke-width="1.6"/>
          <path d="M9 18 h18" stroke="#4d4d4f" stroke-width="1.6"/>
        </svg>
        www.qorvil.example
      </li>
    </ul>
  </section>

  <div class="brand" style="position:absolute; left:24px; top:800px; color:var(--grey); font-size:64px;">
    <span class="brand__square" style="width:44px; height:44px; background:var(--green);"></span>qorvil
  </div>
</body>
</html>
```